Pregnancy and Fertility Information Website

Hello Designers,
I need a website which provide tips and information about healthy and happy pregnancy. My website name is Lorvin medical.

The website should provide all the information needed throughout pregnancy and beyond ranging from pregnancy tracking tools and articles about common pregnancy concerns and what to expect during pregnancy,etc.
The details about first trimester, second trimester and third trimester should be highlighted in the website.

Top Navigation
Home, Fertility, Pregnancy basics, Articles, Tips and News

I'm looking for a simple and clean design which involves captivating images and colors but it shouldn't be crowded. The design must be professional and modern. An easy to navigate layout is a must.

Green, violet, blue and light yellow colors are my favorites but i'm open to other options.

Any questions. Kindly ask

Industry/Entity Type

Medical

```html
<!DOCTYPE html>
<html lang="en">
<head>
<meta charset="utf-8">
<title>Lorvin Medical – Pregnancy &amp; Fertility</title>
<link href="https://fonts.googleapis.com/css2?family=Lustria&family=Lato:wght@400;700&display=swap" rel="stylesheet">
<style>
:root{
  --green:#2bb34f;
  --green-dark:#24a044;
  --blue:#1b74c2;
  --blue-dark:#135ea3;
  --ink:#333333;
  --muted:#666666;
  --line:#dddddd;
  --dark:#262626;
  --darker:#1c1c1c;
  --paper:#ffffff;
  --soft:#f6f6f6;
}
*{box-sizing:border-box;margin:0;padding:0}
html,body{width:1200px;height:3838px;overflow:hidden;background:var(--paper)}
body{position:relative;font-family:"Lato",Arial,sans-serif;color:var(--ink);font-size:14px}
.abs{position:absolute}
.serif{font-family:"Lustria",Georgia,serif}
.photo{position:absolute}

/* header */
.topbar{left:0;top:0;width:1200px;height:72px;background:var(--paper)}
.phone{left:614px;top:22px;display:flex;align-items:center;gap:10px;font-size:18px;color:var(--ink)}
.phone .ic{width:28px;height:28px;border-radius:50%;background:var(--green);display:flex;align-items:center;justify-content:center}
.search{left:780px;top:20px;width:232px;height:32px;border:1px solid var(--line);font-size:13px;color:#999;padding:7px 10px}
.search-btn{left:1022px;top:20px;width:74px;height:32px;background:var(--green);color:#fff;font-size:14px;text-align:center;line-height:32px}
.nav{left:0;top:72px;width:1200px;height:41px;background:var(--blue)}
.nav a{position:absolute;top:0;line-height:41px;color:#fff;font-size:13px;font-weight:700;text-decoration:none;letter-spacing:.5px}
.nav a.active{border-bottom:3px solid #fff;line-height:38px}
.brand{left:97px;top:5px;width:184px;height:184px;border-radius:50%;background:var(--paper);box-shadow:0 2px 10px rgba(0,0,0,.2);display:flex;align-items:center;justify-content:center;flex-direction:column;z-index:3}
.brand span{font-family:"Lustria",Georgia,serif;font-size:30px;color:var(--blue);line-height:1.1;text-align:center}

/* hero */
.hero{left:0;top:113px;width:1200px;height:539px;background:linear-gradient(100deg,#e9e3d6 0%,#ddd2c0 30%,#b84a3a 52%,#9f3529 62%,#c8b8a4 80%,#e6e1d6 100%)}
.hero h1{left:102px;top:308px;font-size:34px;font-weight:400;color:#222}
.hero p{left:102px;top:356px;width:420px;font-size:13px;line-height:18px;color:#333}
.btn{display:block;background:var(--green);color:#fff;font-size:14px;font-weight:700;text-align:center;border-radius:2px}
.hero .btn{left:102px;top:414px;width:146px;height:39px;line-height:39px}

/* quick contact */
.qc{left:770px;top:591px;width:330px;height:432px;background:var(--paper);box-shadow:0 0 10px rgba(0,0,0,.12);z-index:2}
.qc h3{position:absolute;left:0;top:18px;width:100%;text-align:center;font-size:24px;font-weight:400;color:var(--blue)}
.qc .sub{position:absolute;left:0;top:52px;width:100%;text-align:center;font-size:12px;color:var(--muted)}
.field{position:absolute;border:1px solid var(--line);background:#fff;font-size:12px;color:#888;padding:10px 12px}
.qc .field{left:20px;width:287px;height:36px}
.qc .btn{position:absolute;left:20px;top:368px;width:287px;height:39px;line-height:39px;font-size:15px}

/* welcome */
.welcome h2{left:100px;top:694px;font-size:30px;font-weight:400;color:var(--blue)}
.rule{height:1px;background:var(--line)}
.rule-mark{width:26px;height:14px;border:2px solid #aaa;border-radius:7px;background:#fff}
.welcome .lead{left:100px;top:778px;width:640px;font-size:14px;font-weight:700;color:#222}
.welcome .body{left:100px;top:805px;width:650px;font-size:13px;line-height:22px;color:#444}
.welcome .btn{left:100px;top:987px;width:120px;height:37px;line-height:37px}

.section-title{left:0;width:1200px;text-align:center;font-size:30px;font-weight:400;color:var(--blue)}

/* trimester cards */
.tri{top:1177px;height:427px;background:var(--paper);box-shadow:0 0 8px rgba(0,0,0,.13);text-align:center}
.tri h4{position:absolute;left:0;width:100%;font-size:19px;font-weight:400;color:#222}
.tri p{position:absolute;left:40px;right:40px;font-size:13px;line-height:21px;color:#555}
.tri .pic{position:absolute;left:0;width:100%;height:250px}
.badge{position:absolute;width:44px;height:44px;border-radius:50%;background:#fff;border:2px solid #cfe3f4;display:flex;align-items:center;justify-content:center}
.tri .line-g{position:absolute;left:50%;margin-left:-20px;width:40px;height:2px;background:var(--green)}

/* green band */
.band{left:0;top:1658px;width:1200px;height:273px;background:linear-gradient(90deg,#6f8a4d,#a8b97c 40%,#c9cdb2 65%,#5a7140)}
.band-box{top:1709px;height:171px;background:rgba(43,179,79,.85);color:#fff}
.band-box h4{position:absolute;left:118px;top:26px;font-size:22px;font-weight:400}
.band-box p{position:absolute;left:118px;top:58px;right:20px;font-size:13px;line-height:20px}
.band-box .ring{position:absolute;left:28px;top:34px;width:62px;height:62px;border-radius:50%;border:2px solid #fff;display:flex;align-items:center;justify-content:center}

/* tools */
.tool{top:2078px;width:214px;height:214px;border-radius:50%;border:3px solid var(--blue);background:#fff;text-align:center}
.tool .lbl{position:absolute;left:0;top:142px;width:100%;font-family:"Lustria",Georgia,serif;font-size:15px;line-height:18px;color:var(--blue)}
.tool svg{position:absolute;left:72px;top:50px}
.chev{top:2160px}

/* articles */
.articles-band{left:0;top:2341px;width:1200px;height:345px;background:linear-gradient(90deg,#2a2a2a,#3b3b3b 50%,#262626)}
.art{top:2540px;width:322px;height:361px;background:#fff;box-shadow:0 0 8px rgba(0,0,0,.15)}
.art .pic{position:absolute;left:10px;top:12px;width:302px;height:166px}
.art .date{position:absolute;left:10px;top:160px;background:var(--green);color:#fff;font-size:12px;font-weight:700;padding:4px 12px}
.art h5{position:absolute;left:14px;top:206px;font-size:14px;font-weight:700;color:#222}
.art .meta{position:absolute;left:14px;top:236px;font-size:12px;color:#555;display:flex;gap:24px;align-items:center}
.art p{position:absolute;left:14px;right:14px;top:264px;font-size:12.5px;line-height:19px;color:#666}

/* testimonials */
.quote{left:225px;top:3032px;width:750px;text-align:center;font-size:13px;line-height:22px;color:#444}
.qmark{top:3015px;font-family:"Lustria",Georgia,serif;font-size:120px;line-height:1;color:#d5d5d5}
.who{left:0;top:3125px;width:1200px;text-align:center;font-size:14px;font-weight:700;color:var(--green)}
.avatar{border-radius:50%;border:3px solid #fff;box-shadow:0 0 6px rgba(0,0,0,.2)}

/* newsletter */
.news{left:0;top:3313px;width:1200px;height:89px;background:var(--green)}
.news .txt{left:179px;top:28px;font-family:"Lustria",Georgia,serif;font-size:24px;color:#fff}
.news .inp{left:501px;top:26px;width:428px;height:38px;background:#fff;font-size:13px;color:#888;padding:11px 12px}
.news .btn2{left:954px;top:26px;width:141px;height:38px;border:2px solid #fff;color:#fff;font-size:15px;font-weight:700;text-align:center;line-height:34px;letter-spacing:1px}

/* footer */
.map{left:0;top:3402px;width:460px;height:391px;background:linear-gradient(135deg,#e9eadf,#dcdccf 50%,#e6e5da)}
.f-mid{left:460px;top:3402px;width:346px;height:391px;background:var(--dark)}
.f-right{left:806px;top:3402px;width:394px;height:391px;background:var(--darker)}
.f-h{font-family:"Lustria",Georgia,serif;font-size:23px;color:#fff}
.f-row{left:504px;display:flex;gap:16px;color:#ddd;font-size:12.5px;line-height:17px}
.f-row .ic{flex:none;width:24px;display:flex;justify-content:center}
.f-right .field{left:41px;width:253px;height:38px;background:#fff;border:none}
.f-btn{left:847px;top:3694px;width:163px;height:36px;line-height:36px;background:var(--blue);color:#fff;text-align:center;font-size:14px;font-weight:700}
.dot{width:24px;height:24px;border-radius:50%}
.bottom{left:0;top:3793px;width:1200px;height:45px;background:#111;color:#ccc;font-size:12.5px}
</style>
</head>
<body>

<!-- header -->
<div class="abs topbar"></div>
<div class="abs phone"><span class="ic"><svg width="14" height="14" viewBox="0 0 24 24"><path fill="#fff" d="M6.6 10.8a15 15 0 0 0 6.6 6.6l2.2-2.2c.3-.3.7-.4 1-.2 1.1.4 2.3.6 3.6.6.6 0 1 .4 1 1V20c0 .6-.4 1-1 1A17 17 0 0 1 3 4c0-.6.4-1 1-1h3.5c.6 0 1 .4 1 1 0 1.3.2 2.5.6 3.6.1.3 0 .7-.2 1z"/></svg></span>123-456-7890</div>
<div class="abs search">Search...</div>
<div class="abs search-btn">Search</div>
<nav class="abs nav">
  <a class="active" style="left:327px">HOME</a>
  <a style="left:486px">FERTILITY</a>
  <a style="left:627px">PREGNANCY BASICS</a>
  <a style="left:813px">ARTICLES</a>
  <a style="left:952px">TIPS</a>
  <a style="left:1058px">NEWS</a>
</nav>
<div class="abs brand"><span>Lorvin<br>medical</span></div>

<!-- hero -->
<section class="abs hero" role="img" aria-label="Photo of a pregnant woman in a red dress holding her belly"></section>
<h1 class="abs serif" style="left:102px;top:308px;font-size:34px;font-weight:400;color:#222">Feel Safe With Mom’s Care</h1>
<p class="abs" style="left:102px;top:356px;width:420px;font-size:13px;line-height:18px;color:#333">Lorem ipsum dolor sit amet, consectetuer adipiscing elit, sed diamest nonummy nibh euismod tincidunt ut laoreet dolore magna.</p>
<a class="abs btn" style="left:102px;top:414px;width:146px;height:39px;line-height:39px">CONTACT NOW</a>

<!-- quick contact -->
<aside class="abs qc">
  <h3 class="serif">Quick Contact</h3>
  <div class="sub">Fill out the form below for your Contact.</div>
  <div class="field" style="top:92px">Full Name</div>
  <div class="field" style="top:138px">Email Address</div>
  <div class="field" style="top:184px">Phone Number</div>
  <div class="field" style="top:230px;height:120px">Message</div>
  <a class="btn">SUBMIT</a>
</aside>

<!-- welcome -->
<div class="welcome">
  <h2 class="abs serif">Welcome To Lorvin Medical</h2>
  <div class="abs rule" style="left:100px;top:752px;width:668px"></div>
  <div class="abs rule-mark" style="left:102px;top:745px"></div>
  <p class="abs lead">Ut enim ad minim veniam, quis nostrud exercitation ullamco laboris nisi ut aliquip ex ea commodo</p>
  <p class="abs body">Lorem ipsum dolor sit amet, consectetuer adipiscing elit, sed diam nonummy nibh euismod tincidunt ut laoreet dolore magna aliquam erat volutpat. Ut wisi enim ad minim veniam, quis nostrud exerci tation ullamcorper suscipit lobortis nisl ut aliquip ex ea commodo consequat. Duis autem vel eum iriure dolor in hendrerit in vulputate velit esse molestie consequat, vel illum dolore eu feugiat nulla facilisis at vero eros et accumsan et iusto odio Nemo enim ipsam voluptatem quia voluptas sit aspernatur aut odit aut fugit, sed quia consequuntur magni dolores eos qui ratione voluptatem sequi nesciunt. Neque porro quisquam est, qui dolorem ipsum quia dolor sit amet, consectetur, adipisci velit.</p>
  <a class="abs btn">READ MORE</a>
</div>

<!-- trimester -->
<h2 class="abs section-title serif" style="top:1070px">Pregnancy Trimester</h2>
<div class="abs rule" style="left:300px;top:1133px;width:600px"></div>
<div class="abs rule-mark" style="left:587px;top:1126px"></div>

<article class="abs tri" style="left:100px;width:317px">
  <div class="pic" role="img" aria-label="Photo of hands holding a pregnancy test" style="top:0;background:linear-gradient(135deg,#8a8a8a,#d8b7a0 55%,#bfa08a)"></div>
  <div class="badge" style="left:136px;top:228px"><svg width="20" height="20" viewBox="0 0 24 24"><circle cx="12" cy="12" r="8" fill="none" stroke="#1b74c2" stroke-width="2"/></svg></div>
  <h4 class="serif" style="top:292px">First Trimester</h4>
  <div class="line-g" style="top:322px"></div>
  <p style="top:336px">Lorem ipsum dolor sit amet, consectetuer adipiscing elit.</p>
</article>

<article class="abs tri" style="left:443px;width:314px">
  <h4 class="serif" style="top:40px">Second Trimester</h4>
  <p style="top:82px">Lorem ipsum dolor sit amet, consectetuer adipiscing elit.</p>
  <div class="pic" role="img" aria-label="Photo of a pregnant woman beside a crib with a teddy bear" style="top:174px;height:253px;background:linear-gradient(135deg,#d9d4cc,#a8c9c8 50%,#7fb3b2)"></div>
  <div class="badge" style="left:135px;top:152px"><svg width="20" height="20" viewBox="0 0 24 24"><circle cx="12" cy="12" r="8" fill="none" stroke="#1b74c2" stroke-width="2"/></svg></div>
</article>

<article class="abs tri" style="left:785px;width:315px">
  <div class="pic" role="img" aria-label="Photo of a pregnant belly in a white top" style="top:0;background:linear-gradient(135deg,#5b3a2a,#f1efe9 45%,#6b4432)"></div>
  <div class="badge" style="left:135px;top:228px"><svg width="20" height="20" viewBox="0 0 24 24"><circle cx="12" cy="12" r="8" fill="none" stroke="#1b74c2" stroke-width="2"/></svg></div>
  <h4 class="serif" style="top:292px">Third Trimester</h4>
  <div class="line-g" style="top:322px"></div>
  <p style="top:336px">Lorem ipsum dolor sit amet, consectetuer adipiscing elit.</p>
</article>

<!-- green band -->
<section class="abs band" role="img" aria-label="Photo of a pregnant woman sitting in green grass"></section>
<div class="abs band-box" style="left:128px;width:453px">
  <div class="ring"><svg width="28" height="28" viewBox="0 0 24 24"><circle cx="12" cy="12" r="7" fill="none" stroke="#fff" stroke-width="2"/></svg></div>
  <h4 class="serif">Fertility</h4>
  <p>Lorem ipsum dolor sit amet, consectetuer adipiscing elit, sed do eiusmod tempor incididunt ut labore et dolore magna aliqua, Ut enim ad minim veniam ...[+]</p>
</div>
<div class="abs band-box" style="left:627px;width:447px">
  <div class="ring"><svg width="28" height="28" viewBox="0 0 24 24"><circle cx="12" cy="12" r="7" fill="none" stroke="#fff" stroke-width="2"/></svg></div>
  <h4 class="serif">Pregnancy Basics</h4>
  <p>Lorem ipsum dolor sit amet, consectetuer adipiscing elit, sed do eiusmod tempor incididunt ut labore et dolore magna aliqua, Ut enim ad minim veniam ...[+]</p>
</div>

<!-- tools -->
<h2 class="abs section-title serif" style="top:1973px">Popular Tools</h2>
<div class="abs rule" style="left:300px;top:2039px;width:600px"></div>
<div class="abs rule-mark" style="left:587px;top:2032px"></div>
<svg class="abs chev" style="left:50px" width="20" height="50" viewBox="0 0 20 50"><path d="M16 2 4 25l12 23" fill="none" stroke="#bbb" stroke-width="2"/></svg>
<svg class="abs chev" style="left:1125px" width="20" height="50" viewBox="0 0 20 50"><path d="M4 2l12 23L4 48" fill="none" stroke="#bbb" stroke-width="2"/></svg>

<div class="abs tool" style="left:123px">
  <svg width="70" height="70" viewBox="0 0 70 70"><rect x="8" y="12" width="54" height="50" rx="3" fill="none" stroke="#1b74c2" stroke-width="4"/><rect x="8" y="12" width="54" height="12" fill="#1b74c2"/><g fill="#1b74c2"><rect x="16" y="30" width="8" height="8"/><rect x="31" y="30" width="8" height="8"/><rect x="46" y="30" width="8" height="8"/><rect x="16" y="44" width="8" height="8"/><rect x="31" y="44" width="8" height="8"/></g></svg>
  <div class="lbl">Due Date<br>Calculator</div>
</div>
<div class="abs tool" style="left:366px">
  <svg width="70" height="70" viewBox="0 0 70 70"><circle cx="35" cy="18" r="12" fill="#1b74c2"/><rect x="20" y="34" width="30" height="26" rx="8" fill="#1b74c2"/></svg>
  <div class="lbl">Baby Names<br>Finder</div>
</div>
<div class="abs tool" style="left:617px">
  <svg width="70" height="70" viewBox="0 0 70 70"><circle cx="35" cy="35" r="28" fill="none" stroke="#9cc3e6" stroke-width="4" stroke-dasharray="4 4"/><path d="M35 35V10a25 25 0 0 1 22 37z" fill="#1b74c2"/></svg>
  <div class="lbl">Ovulation<br>Calculator</div>
</div>
<div class="abs tool" style="left:868px">
  <svg width="70" height="70" viewBox="0 0 70 70"><circle cx="30" cy="16" r="11" fill="#1b74c2"/><path d="M18 30h22c10 0 18 8 18 18v14H18z" fill="#1b74c2"/></svg>
  <div class="lbl">Pregnancy Week<br>By Week</div>
</div>

<!-- articles -->
<section class="abs articles-band" role="img" aria-label="Dark photo of a pregnant woman by a window"></section>
<h2 class="abs section-title serif" style="top:2385px;color:#fff">Our Articles</h2>
<div class="abs rule" style="left:185px;top:2451px;width:830px;background:#666"></div>
<div class="abs rule-mark" style="left:587px;top:2444px;background:#333;border-color:#999"></div>
<svg class="abs" style="left:565px;top:2497px" width="70" height="20" viewBox="0 0 70 20"><path d="M4 10h16M4 10l6-5M4 10l6 5" stroke="#999" stroke-width="2" fill="none"/><path d="M35 2v16" stroke="#666"/><path d="M66 10H50m16 0-6-5m6 5-6 5" stroke="#999" stroke-width="2" fill="none"/></svg>

<article class="abs art" style="left:100px">
  <div class="pic" role="img" aria-label="Photo of a pregnant woman in a white shirt" style="background:linear-gradient(135deg,#f0f0f0,#cfcfcf 50%,#4a4a4a)"></div>
  <span class="date">10 Feb, 2016</span>
  <h5>Ut enim ad minim veniam, quis</h5>
  <div class="meta"><span>👁&nbsp; 5605 Times</span><span>○&nbsp; 0Comment</span></div>
  <p>Lorem ipsum dolor sit amet, consectetur adipiscing elit. Integer venenatis tincidunt elit, aliquam semper quam pulvinar id.</p>
</article>
<article class="abs art" style="left:440px">
  <div class="pic" role="img" aria-label="Photo of fresh fruit and vegetables beside a pregnant belly" style="background:linear-gradient(135deg,#d9e8d0,#8fbf64 45%,#e9e1d8)"></div>
  <span class="date">10 Feb, 2016</span>
  <h5>Ut enim ad minim veniam, quis</h5>
  <div class="meta"><span>👁&nbsp; 5605 Times</span><span>○&nbsp; 0Comment</span></div>
  <p>Lorem ipsum dolor sit amet, consectetur adipiscing elit. Integer venenatis tincidunt elit, aliquam semper quam pulvinar id.</p>
</article>
<article class="abs art" style="left:780px">
  <div class="pic" role="img" aria-label="Photo of pregnant women exercising on fitness balls" style="background:linear-gradient(135deg,#ece4df,#d7b8d8 50%,#b57fc1)"></div>
  <span class="date">10 Feb, 2016</span>
  <h5>Ut enim ad minim veniam, quis</h5>
  <div class="meta"><span>👁&nbsp; 5605 Times</span><span>○&nbsp; 0Comment</span></div>
  <p>Lorem ipsum dolor sit amet, consectetur adipiscing elit. Integer venenatis tincidunt elit, aliquam semper quam pulvinar id.</p>
</article>

<!-- testimonials -->
<h2 class="abs section-title serif" style="top:2937px">Client Testimonials</h2>
<div class="abs qmark" style="left:160px">“</div>
<div class="abs qmark" style="left:990px">”</div>
<p class="abs quote">Fusce elementum, nulla vel pellentes consequat, ante nulla hendrerit arcu, ac tincidunt mauris lacus sed leo. vamus suscipit molestie vestibulum. Lorem ipsum dolor sit amet. Fusce elementum, nulla vel pellentes consequat, ante nulla hendrerit arcu, ac tincidunt mauris lacus sed leo. vamus suscipit molestie. Fusce elementum, nulla vel</p>
<div class="abs who">Maren</div>
<div class="abs avatar" role="img" aria-label="Client portrait" style="left:441px;top:3132px;width:84px;height:84px;background:linear-gradient(135deg,#c9a48a,#7a4f3a)"></div>
<div class="abs avatar" role="img" aria-label="Client portrait" style="left:553px;top:3120px;width:96px;height:96px;background:linear-gradient(135deg,#e0c2a6,#8c5a3e)"></div>
<div class="abs avatar" role="img" aria-label="Client portrait" style="left:684px;top:3132px;width:84px;height:84px;background:linear-gradient(135deg,#d8b79c,#6e4a38)"></div>

<!-- newsletter -->
<section class="abs news">
  <svg class="abs" style="left:94px;top:22px" width="48" height="48" viewBox="0 0 48 48"><circle cx="24" cy="24" r="22" fill="none" stroke="#fff" stroke-width="2"/><rect x="13" y="16" width="22" height="16" fill="none" stroke="#fff" stroke-width="2"/><path d="m13 16 11 9 11-9" fill="none" stroke="#fff" stroke-width="2"/></svg>
  <div class="abs txt">Newsletter Signup</div>
  <svg class="abs" style="left:445px;top:16px" width="26" height="58" viewBox="0 0 26 58"><path d="M3 3l20 26L3 55" fill="none" stroke="#fff" stroke-width="3"/></svg>
  <div class="abs inp">Your e-mail</div>
  <div class="abs btn2">SIGN UP</div>
</section>

<!-- footer -->
<section class="abs map" role="img" aria-label="Street map showing the clinic location"></section>
<svg class="abs" style="left:180px;top:3570px" width="30" height="42" viewBox="0 0 30 42"><path d="M15 41C15 41 2 24 2 15a13 13 0 0 1 26 0c0 9-13 26-13 26z" fill="#1b74c2"/><circle cx="15" cy="15" r="5" fill="#fff"/></svg>
<div class="abs f-mid"></div>
<svg class="abs" style="left:436px;top:3580px" width="24" height="48" viewBox="0 0 24 48"><path d="M24 0v48L0 24z" fill="#262626"/></svg>
<div class="abs f-right"></div>

<div class="abs f-h" style="left:504px;top:3450px">Get In Touch</div>
<div class="abs f-row" style="top:3500px"><span class="ic"><svg width="16" height="22" viewBox="0 0 16 22"><path d="M8 21S1 12 1 8a7 7 0 0 1 14 0c0 4-7 13-7 13z" fill="#1b74c2"/><circle cx="8" cy="8" r="2.5" fill="#262626"/></svg></span><span><b style="color:#fff">Lorvin Medical</b><br>Lorem ipsum dolor sit amet, sed<br>consectetur adipiscing elit sed.</span></div>
<div class="abs f-row" style="top:3584px;align-items:center"><span class="ic"><svg width="18" height="18" viewBox="0 0 24 24"><path fill="#1b74c2" d="M6.6 10.8a15 15 0 0 0 6.6 6.6l2.2-2.2c.3-.3.7-.4 1-.2 1.1.4 2.3.6 3.6.6.6 0 1 .4 1 1V20c0 .6-.4 1-1 1A17 17 0 0 1 3 4c0-.6.4-1 1-1h3.5c.6 0 1 .4 1 1 0 1.3.2 2.5.6 3.6.1.3 0 .7-.2 1z"/></svg></span><span style="font-size:15px">123.456.7890</span></div>
<div class="abs f-row" style="top:3654px;align-items:center"><span class="ic"><svg width="20" height="16" viewBox="0 0 20 16"><rect x="1" y="1" width="18" height="14" fill="#1b74c2"/><path d="m1 1 9 8 9-8" fill="none" stroke="#262626" stroke-width="1.5"/></svg></span><span>info@lorvinmedical.com</span></div>
<div class="abs" style="left:502px;top:3722px;display:flex;gap:8px">
  <span class="dot" style="background:#3b5998"></span><span class="dot" style="background:#1da1f2"></span><span class="dot" style="background:#f7931e"></span>
</div>

<div class="abs f-h" style="left:847px;top:3450px">Quick Contact</div>
<div class="abs field" style="left:847px;top:3502px;width:253px;height:38px;border:none">Your name</div>
<div class="abs field" style="left:847px;top:3553px;width:253px;height:38px;border:none">Your e-mail</div>
<div class="abs field" style="left:847px;top:3607px;width:253px;height:72px;border:none">Your message</div>
<div class="abs f-btn">SUBMIT</div>

<footer class="abs bottom">
  <span class="abs" style="left:100px;top:15px">Copyright © 2016 Lorvin Medical. All Rights Reserved.</span>
  <span class="abs" style="left:832px;top:15px">Privacy Policy</span>
  <span class="abs" style="left:948px;top:13px;color:#777">|</span>
  <span class="abs" style="left:970px;top:15px">Terms &amp; Conditions</span>
</footer>

</body>
</html>
```